Business card for someone who trains leaders
Organizational Development Consultant Business Card - Consulting
Organizational Development Consultant Business Card
Bright & Fun-filled
Darla Quinby
Capacity Development Adviser
(NO ADDRESS IS LISTED ON CARD)
darla@vrmthrivewell.com
www.netprofile/in/marlowquinby
I want a business card that says professional but not too corporate. I want it to only use the colors on my logo (plus white of course). I like the look of cards that have some black backgrounds, but I'm open to a lot of different looks - as long as it meshes well with the look and feel of the business card. I don't want anything too busy, but yet want something that stands out a bit.
Where Will Your Growth Lead? Let VRM Thrivewell help you find growth through organizational development, leadership coaching, and much more!
marlowquinby marlowquinby
Please don't submit generic samples with someone else's information. I'm only interested in seeing completed business cards with the information I included in the creative brief.
I would like to see some designs that are on a white background as well as a black background. I'm not sold either way, but want to see a variety. Also, on the creative brief, I left off the website. In addition to my netprofile profile, I also want the website www.vrmthrivewell.com.

```html
<!DOCTYPE html>
<html lang="en">
<head>
<meta charset="utf-8">
<title>VRM Thrivewell Stationery</title>
<link href="https://fonts.googleapis.com/css2?family=Montserrat:wght@400;600&display=swap" rel="stylesheet">
<style>
  :root {
    --stage: #5d5d5d;
    --paper: #ffffff;
    --ink: #3a3a4a;
    --muted: #8a8a98;
    --blue: #2c3fc4;
    --violet: #6b36a8;
    --deep: #23206e;
    --fold: #d9d9de;
    --wash: rgba(255,255,255,0.14);
    --tint: rgba(107,54,168,0.12);
  }
  * { box-sizing: border-box; margin: 0; padding: 0; }
  html, body { width: 1200px; height: 325px; overflow: hidden; }
  body {
    background: var(--stage);
    font-family: "Montserrat", sans-serif;
    color: var(--ink);
    position: relative;
  }
  .piece { position: absolute; background: var(--paper); overflow: hidden; }
  .brand { display: flex; align-items: center; gap: 3px; }
  .brand-dot { border-radius: 50%; background: var(--blue); flex: none; }
  .brand-name { font-weight: 600; color: var(--blue); white-space: nowrap; }
  .gradient { background: linear-gradient(160deg, var(--violet), var(--blue) 60%, var(--deep)); }
  .ring { position: absolute; border-radius: 50%; }
  .small-text { font-size: 3px; line-height: 4.5px; color: var(--muted); white-space: nowrap; }

  /* small business cards */
  .card-front { left: 23px; top: 94px; width: 75px; height: 46px; }
  .card-front .brand { position: absolute; left: 6px; top: 16px; }
  .card-back { left: 23px; top: 147px; width: 75px; height: 46px; }

  /* letterhead */
  .letterhead { left: 105px; top: 42px; width: 180px; height: 258px; }
  .letterhead .band { position: absolute; left: 8px; top: 0; width: 10px; height: 100%; }
  .letterhead .brand { position: absolute; left: 26px; top: 14px; }
  .letterhead .ring { right: -30px; bottom: 20px; width: 110px; height: 110px; background: var(--tint); }
  .letterhead .footer { position: absolute; left: 26px; bottom: 10px; }

  /* envelopes */
  .envelope { position: absolute; }

  /* large business cards */
  .card-name { left: 550px; top: 105px; width: 117px; height: 72px; }
  .card-name .band { position: absolute; left: 0; top: 0; width: 6px; height: 100%; }
  .card-name .brand { position: absolute; left: 12px; top: 8px; }
  .card-name .person { position: absolute; left: 12px; top: 30px; }
  .person-name { font-size: 5px; font-weight: 600; color: var(--ink); }
  .card-logo { left: 550px; top: 190px; width: 117px; height: 68px; }
  .card-logo .brand { position: absolute; left: 14px; top: 28px; }
  .card-logo .ring { right: -14px; bottom: -14px; width: 50px; height: 50px; background: var(--tint); }

  /* presentation folder */
  .folder-left { left: 795px; top: 12px; width: 190px; height: 304px; }
  .folder-left .ring { left: 40px; top: 40px; width: 170px; height: 170px; background: var(--wash); }
  .folder-left .note { position: absolute; left: 14px; bottom: 60px; color: rgba(255,255,255,0.7); }
  .folder-right { left: 985px; top: 12px; width: 185px; height: 304px; }
  .folder-right .band { position: absolute; left: 0; top: 0; width: 14px; height: 100%; }
  .folder-right .brand { position: absolute; left: 24px; top: 16px; }
  .folder-right .ring { right: -40px; top: 40px; width: 170px; height: 170px; background: var(--tint); }
  .folder-right .pocket { position: absolute; left: 0; bottom: 0; }
</style>
</head>
<body>

  <div class="piece card-front">
    <div class="brand"><span class="brand-dot" style="width:8px;height:8px"></span><span class="brand-name" style="font-size:5px">VRM Thrivewell</span></div>
  </div>
  <div class="piece card-back gradient">
    <div class="ring" style="right:-10px;top:-6px;width:40px;height:40px;background:var(--wash)"></div>
  </div>

  <div class="piece letterhead">
    <div class="band gradient"></div>
    <div class="brand"><span class="brand-dot" style="width:9px;height:9px"></span><span class="brand-name" style="font-size:5.5px">VRM Thrivewell</span></div>
    <div class="ring"></div>
    <div class="footer small-text">www.vrmthrivewell.com</div>
  </div>

  <svg class="envelope" style="left:300px;top:42px" width="234" height="262" viewBox="0 0 234 262" aria-hidden="true">
    <rect x="0" y="0" width="234" height="92" fill="var(--paper)"/>
    <path d="M0 0 L117 40 L234 0 Z" fill="var(--deep)" opacity="0.85"/>
    <circle cx="117" cy="26" r="8" fill="var(--paper)"/>
    <rect x="0" y="98" width="234" height="92" fill="var(--paper)"/>
    <path d="M0 98 L117 140 L234 98" fill="none" stroke="var(--fold)" stroke-width="2"/>
    <path d="M0 190 L100 150 M234 190 L134 150" stroke="var(--fold)" stroke-width="1.5"/>
    <circle cx="117" cy="138" r="7" fill="var(--blue)"/>
    <rect x="0" y="196" width="234" height="66" fill="var(--paper)"/>
    <path d="M0 196 L117 236 L234 196" fill="none" stroke="var(--fold)" stroke-width="1.5"/>
    <path d="M0 262 L100 226 M234 262 L134 226" stroke="var(--fold)" stroke-width="1"/>
  </svg>

  <div class="piece card-name">
    <div class="band gradient"></div>
    <div class="brand"><span class="brand-dot" style="width:7px;height:7px"></span><span class="brand-name" style="font-size:4.5px">VRM Thrivewell</span></div>
    <div class="person">
      <p class="person-name">Darla Quinby</p>
      <p class="small-text">Capacity Development Adviser</p>
      <p class="small-text">darla@vrmthrivewell.com</p>
      <p class="small-text">www.netprofile/in/marlowquinby</p>
      <p class="small-text">www.vrmthrivewell.com</p>
    </div>
  </div>
  <div class="piece card-logo">
    <div class="brand"><span class="brand-dot" style="width:9px;height:9px"></span><span class="brand-name" style="font-size:6px">VRM Thrivewell</span></div>
    <div class="ring"></div>
  </div>

  <div class="piece folder-left gradient">
    <div class="ring"></div>
    <div class="note small-text">
      <p>Organizational development and leadership coaching</p>
      <p>www.vrmthrivewell.com</p>
    </div>
  </div>
  <div class="piece folder-right">
    <div class="band gradient"></div>
    <div class="brand"><span class="brand-dot" style="width:12px;height:12px"></span><span class="brand-name" style="font-size:7px">VRM Thrivewell</span></div>
    <div class="ring"></div>
    <svg class="pocket" width="185" height="110" viewBox="0 0 185 110" aria-hidden="true">
      <defs>
        <linearGradient id="pocket-fill" x1="0" y1="0" x2="1" y2="1">
          <stop offset="0" stop-color="var(--violet)"/>
          <stop offset="1" stop-color="var(--blue)"/>
        </linearGradient>
      </defs>
      <path d="M0 30 L185 0 L185 110 L0 110 Z" fill="url(#pocket-fill)"/>
    </svg>
  </div>

</body>
</html>
```